Trying to make a small (4.25" x 5.50") re-elect sticker for a congressman in california. The congressmans name is Calder Voss and we would like to change his last name to "Vossovich". Basically we believe his relationship to Pike/Brevik should be reflected in this poster with russia undertones.

The idea behind this project is to reflect Calder Voss as a political puppet of Harlan Pike who is also a puppet of Russian president Brevik.
We do not support Calder Voss as our elected official and believe him to be a traitor to our district and a traitor to our country.
Trying to make a small (4.25" x 5.50") re-elect sticker for a congressman in California. The congressman's name is Calder Voss and we would like to change his last name to "Vossovich". Basically we believe his relationship to Pike/Brevik should be reflected in this poster with Russia undertones.

Trying to make a small (4.25" x 5.50") re-elect sticker for a congressman in California. The congressman's name is Calder Voss and we would like to change his last name to "Vossovich". Basically we believe his relationship to Pike/Brevik should be reflected in this poster with Russian undertones.

I have never done this type of project before so any advise would be helpful,any questions just email me thanks.
Owen

Owen

Target Market(s)

For political grass roots campaign.

Industry/Entity Type

Political

Colors

Designer to choose colors to be used in the design.

Requirements
Must have
• Picture of Calder Voss. Re-elect (переизбрание). Change last name to Vossovich
Nice to have
• Maybe the hammer and sickle logo someplace but not too obvious
Should not have
• Nothing obscene or offensiveпереизбрание

```html
<!DOCTYPE html>
<html lang="en">
<head>
<meta charset="utf-8">
<title>The Great Puppet – Calder Vossovich</title>
<link rel="stylesheet" href="https://fonts.googleapis.com/css2?family=Bebas+Neue&display=swap">
<style>
  :root {
    --page-bg: #f4f4f4;
    --field-deep: #2e3191;
    --field-light: #0a70c0;
    --flag-red: #ed1c24;
    --paper-white: #ffffff;
    --skin-light: #f1c9ad;
    --skin-mid: #e4ae8f;
    --sleeve-blue: #8fb3dc;
    --suit-dark: #1d1d1f;
    --shirt-blue: #7fb2e8;
  }
  html, body {
    margin: 0;
    padding: 0;
    width: 1200px;
    height: 1200px;
    overflow: hidden;
    background: var(--page-bg);
  }
  .canvas {
    width: 1200px;
    height: 1200px;
    display: flex;
    justify-content: center;
    align-items: center;
  }
  .sticker {
    width: 928px;
    height: 1200px;
    display: block;
  }
  .headline {
    font-family: "Bebas Neue", "Oswald", sans-serif;
  }
  .headline-white { fill: var(--paper-white); }
  .headline-red {
    fill: var(--flag-red);
    stroke: var(--paper-white);
    stroke-width: 3;
    paint-order: stroke;
  }
</style>
</head>
<body>
<main class="canvas">
  <svg class="sticker" viewBox="0 0 928 1200" xmlns="http://www.w3.org/2000/svg">
    <defs>
      <radialGradient id="field-glow" cx="0.6" cy="0.5" r="0.7">
        <stop offset="0" stop-color="var(--field-light)"/>
        <stop offset="1" stop-color="var(--field-deep)"/>
      </radialGradient>
      <linearGradient id="hand-tones" x1="0" y1="0" x2="1" y2="0">
        <stop offset="0" stop-color="var(--skin-light)" stop-opacity="0.35"/>
        <stop offset="0.6" stop-color="var(--skin-mid)" stop-opacity="0.55"/>
        <stop offset="1" stop-color="var(--sleeve-blue)" stop-opacity="0.7"/>
      </linearGradient>
      <linearGradient id="puppet-tones" x1="0" y1="0" x2="0" y2="1">
        <stop offset="0" stop-color="var(--skin-light)" stop-opacity="0.45"/>
        <stop offset="0.3" stop-color="var(--shirt-blue)" stop-opacity="0.4"/>
        <stop offset="0.45" stop-color="var(--suit-dark)" stop-opacity="0.75"/>
        <stop offset="1" stop-color="var(--suit-dark)" stop-opacity="0.85"/>
      </linearGradient>
    </defs>

    <rect class="field" x="0" y="0" width="928" height="1200" fill="url(#field-glow)"/>

    <rect class="hand-illustration" x="5" y="0" width="923" height="270" fill="url(#hand-tones)"
          role="img" aria-label="A hand wearing a red campaign wristband and a red, white and blue striped cuff, holding puppet strings"/>

    <rect class="puppet-illustration" x="0" y="540" width="300" height="615" fill="url(#puppet-tones)"
          role="img" aria-label="Caricature of Calder Voss as a marionette in a black suit and red tie, hanging from strings"/>

    <rect class="base-band" x="0" y="954" width="928" height="215" fill="var(--flag-red)"/>

    <text class="headline headline-white" transform="translate(379,434) rotate(-90)" x="0" y="0"
          font-size="121" textLength="165" lengthAdjust="spacingAndGlyphs">THE</text>
    <text class="headline headline-white" x="395" y="447" font-size="254"
          textLength="502" lengthAdjust="spacingAndGlyphs">GREAT</text>
    <text class="headline headline-white" x="301" y="653" font-size="256"
          textLength="596" lengthAdjust="spacingAndGlyphs">PUPPET</text>
    <text class="headline headline-red" x="294" y="926" font-size="347"
          textLength="576" lengthAdjust="spacingAndGlyphs">CALDER</text>
    <text class="headline headline-white" x="294" y="1145" font-size="237"
          textLength="574" lengthAdjust="spacingAndGlyphs">VOSSOVICH</text>
  </svg>
</main>
</body>
</html>
```